KEB Lau Sound business package.
business cards, stationary, letterhead, envelopes, CD labels and packaging, appointment cards, etc..
Thank you Mr. harven47 !!!!!
CONGRATS 7pixelcrafter
CONGRATS Mr. 7pc!!!!!!!!!!!!!!!!!!
I chose draft #56 as the winner.
I wanted to thank all designers for their great contributions and all your help and great advice.
You guys are all awesome.
I of course wanted to thank Mr. 7pc in particular from the bottom of my heart for always dealing so gracefully and friendly with my sometimes tough to deal with "Mr. Perfectionist" attitude and way of doing things. haha :)
I am super happy with the chosen design.
Fantastic work.
THANK YOU.
Much love to you and your family.
Talor.
@ PH Thank you for your honesty and candor about your likely early decision on the design. I hope all PH's can be as honest and thoughtful. Good luck with your business!!!
It looks like Mr. 7pixelcrafter's draft #48 is going to be the winner.
I know I could always be surprised of course, but I don't think anybody is going to be able to change my mind and beat how I feel about his design.
I know I still have over a day left before this project closes, but... I am only posting this here because I care about your time, talent and energy, and I want to make sure you don't spend extra time and resources on this project if you could be working on other projects where you have a higher likelihood of winning the project.
I am super anxious to see Mr. 7pixelcrafter's revisions I asked for.
My favorite designs btw are:
#20 (all the design AND the business cards), #31 (but not the business cards and not the shirts), #37 and #38
It looks like this is going to go between Mr. 7pixelcrafter and my friend who created the logo Mr. Harven47 for the winning bid.
We seem to have an India vs. India house contest here haha.
At this time: I tend to lean over to really liking #20 and #31 as my favorites.
Tips and pointers:
1) I gravitate towards preferring having the contact info at the bottom of the fax/letterhead (as in #20 and #31)
I have a feeling that the design that is going to win, is going to be the design that has the contact info at the bottom, and the company name more featured on top of the letterhead/fax design.
2) I prefer ligher colors that fit/match as closely as possible to the color of the KEB Lau Sound logo.
3) I tend to prefer having the KEB Lau Sound logo featured.. meaning: larger... on business cards, letterheads, fax pages, actually... everything.
4) I tend to lean towards liking having the big "O" with headphones logo on the lower left corner of fax/letterhead pages as a light background/watermark
5) I REALLY really like it when ALL materials have a certain design element that ties ALL materials together. Which is why I for example REALLY like #20 (ALL the materials have exactly the same design elements
6) I would LOOOOOVEEE to see copies/drafts of my 4 favorite designs mentioned above, with some slight touch of silver added to the white backgrounds of all materials/stationary. (As in the silver-ish kind of background in the original "white/silver background" of the KEB Lau Sound logo file I uploaded for this project)
Fixes:
1) I need to have the 415-738-2261 (cell) number on top of the landline (323 etc) number on all materials. (cell first)
2) I absolutely want the center of the O's in "KEB Lau Sound" to be exactly the same color as the background (on ALL materials). If the background is black, I want the center of the O to be black as well, if it is turquoise, then I want the center of the O to be turquoise as well, etc... etc...
Thank you for all your amazing work.
Much respect and love for all your work and your talent.
Best
First off:
I am SUPER HAPPY with all your submissions. You are ALL doing an amazing job and it is again going to be very hard for me to choose here. :)
So here's some guidance, sharing with you my favorite things I have seen, likes, etc...
Right now my 2 favorite ones are #33 and #31
My favorite color so far is Mr. Harven's #33
Mr Harven, Could I see a copy of the fax sheet and stationary/letterhead with the big O in the lower left corner
1) much lighter in color (kind a like a watermark. My concern is that it might interfere with typed text on the letter as it is now)
2) with that big O moved a bit to the left so the whole symbol is on the page.
3) with the company name/logo bigger on all materials.
(This does not have to be 3 different drafts btw... trying to save you time here... I am looking for one draft that has all these 3 things all together.)
More about #33
I LOVE the simplicity of the footer (bottom of page) you created on the letterhead/footer and fax page.
On the business cards: you did an amazing job on the color of the back of the business card. Keep it that way please haha. However: you know how much I am in love with color of the logo you created: is there any way you can have the logo/business name in the original color (instead of white) on that awesome background you created here?? (not sure if that would work, or if it would be too much of the same color?)
How would it look like if you made the word 'Music" black?
Mr. 7pixelcrafter draft #31
I completely LOVE how you did this smart out of the box thinking thing and made the business cards vertical (which is pretty unusual haha). So cool.
I also really frigging like what you did with the blue hue color lettering in my name and URL on the business cards.
I also adore the design of the fax sheet and letterhead. I really like it's simplicity.
But can I see a draft of the letterhead and fax page: where
1) you make a the company logo top left corner a bit bigger
2) Can you also add the O with head phones in the lower right corner, very lightly (like a watermark type thing)
Lastly: I am trying to figure out how I like the business cards with the company name in the big O.
Part of me is in love with the company logo design, and want to see it bigger and free (meaning: not surrounded by the big O ). I prefer the idea of using that O icon as a lighter background/watermark kind a thing.
Comments for everybody:
1) I need to have my cell phone number and email on the CD labels and on the CD insert sheet.
2) I would like you all to use little icons instead of using the words "cell", "address", "phone", etc...
The reason being that icons are more international: the word "cell" for example in Britain or Australia is confusing, as they call it a "mobile" there.
3) Us a little "house" icon for "address"
4) I want my cell number, to be ABOVE my land line/phone number
5) I want the address LAST. (Think about it: people have short attention spans haha... it's all about marketing and grabbing people... the FIRST thing they want to see is where to get in touch with you right now... your cell phone... not where you live.)
Draft #26 and #27
I like your very smart idea of creating tablature paper, music paper etc... with my logo and business name/logo on. You get extra points sir for that amazing idea. I should have thought of that myself already, but you beat me to it haha.
On the black shirt: I would not put the O logo on the front, as it makes it a bit too heavy and busy, already having my name logo there. I woud make the name logo bigger, and have the big O on the back of the shirt. Also: no tilted O.
On the white top: FANTASTIC artwork with the O logo... I really like the dotted approach you came up with here.
I also like how you picked up on my asking in an earlier post about the more silvery approach I wanted to see examples of.

```html
<!DOCTYPE html>
<html lang="en">
<head>
<meta charset="utf-8">
<title>KEB Lau Sound – CD Label and Sleeve</title>
<link rel="stylesheet" href="https://fonts.googleapis.com/css2?family=Exo+2:wght@400;700;800&family=Open+Sans:wght@400;600&display=swap">
<style>
  :root{
    --backdrop:#d6d8da;
    --blue:#1e9be0;
    --blue-deep:#0d78c2;
    --blue-light:#8fd4f6;
    --blue-pale:#cfeefc;
    --navy:#123a5c;
    --white:#ffffff;
    --sleeve-white:#f1f6f9;
  }
  *{margin:0;padding:0;box-sizing:border-box}
  html,body{width:1200px;height:871px;overflow:hidden}
  body{background:var(--backdrop);font-family:"Open Sans",sans-serif;position:relative}
  .artboard{position:absolute;inset:0}

  /* Folder (left) */
  .folder{position:absolute;left:96px;top:353px;width:492px;height:447px;
    background:linear-gradient(160deg,var(--blue-light) 0%,var(--blue) 55%,var(--blue-deep) 100%);}
  .folder .fold-line{position:absolute;left:195px;top:100px;width:120px;height:2px;background:rgba(18,58,92,.35)}
  .folder .note-art{position:absolute;left:150px;top:75px;width:130px;height:120px;border-radius:40px;
    background:radial-gradient(circle,rgba(255,255,255,.28),rgba(255,255,255,0) 70%)}
  .folder .ring-art{position:absolute;left:120px;top:160px;width:260px;height:240px;border-radius:50%;
    background:radial-gradient(circle,rgba(255,255,255,.22) 0%,rgba(255,255,255,.08) 55%,rgba(255,255,255,0) 72%)}
  .folder .contact{position:absolute;left:0;right:0;top:325px;text-align:center;color:var(--white)}
  .contact .brand-small{font-family:"Exo 2",sans-serif;font-weight:800;font-size:17px;color:var(--navy);margin-bottom:6px;margin-left:-40px}
  .contact .address{font-size:11.5px;line-height:17px;margin-left:-40px}
  .contact .lines{position:absolute;top:100px;left:0;right:0;font-size:11.5px;font-weight:600;white-space:nowrap}
  .contact .lines span{margin:0 5px}

  /* Sleeve (right) */
  .sleeve{position:absolute;left:600px;top:377px;width:504px;height:423px;background:var(--sleeve-white);overflow:hidden}
  .sleeve .band{position:absolute;left:0;bottom:0;width:100%;height:120px}
  .sleeve .star-art{position:absolute;left:18px;top:255px;width:160px;height:110px;border-radius:30px;
    background:radial-gradient(ellipse,rgba(30,155,224,.75),rgba(30,155,224,0) 70%)}
  .sleeve .ring-art{position:absolute;left:265px;top:190px;width:230px;height:210px;border-radius:50%;
    background:radial-gradient(circle,rgba(143,212,246,.55) 0%,rgba(143,212,246,.25) 50%,rgba(143,212,246,0) 72%)}
  .sleeve .note-art{position:absolute;left:370px;top:150px;width:80px;height:70px;border-radius:30px;
    background:radial-gradient(circle,rgba(143,212,246,.5),rgba(143,212,246,0) 70%)}
  .sleeve .brand{position:absolute;left:0;right:0;top:58px;text-align:center;
    font-family:"Exo 2",sans-serif;font-weight:800;font-size:44px;color:var(--blue-deep);letter-spacing:.5px}
  .sleeve .url{position:absolute;left:48px;bottom:48px;font-size:12px;font-weight:600;color:var(--white)}
  .flap{position:absolute;left:600px;top:302px;width:504px;height:140px}

  /* Disc */
  .disc{position:absolute;left:101px;top:5px;width:408px;height:408px}
  .disc .brand{position:absolute;left:0;right:0;top:320px;text-align:center;
    font-family:"Exo 2",sans-serif;font-weight:800;font-size:34px;color:var(--white)}
</style>
</head>
<body>
<main class="artboard">

  <section class="folder" aria-label="CD folder cover">
    <div class="fold-line"></div>
    <div class="note-art" role="img" aria-label="Faint music note decoration"></div>
    <div class="ring-art" role="img" aria-label="Faint circular watermark decoration"></div>
    <div class="contact">
      <p class="brand-small">KEB Lau Sound</p>
      <p class="address">P.O. Box 5817<br>Fairview, CA 90412<br>USA</p>
      <p class="lines"><span>Cell : 415-738-2261</span><span>Phone : 628-304-5190</span><span>Email : talor@keblausound.com</span></p>
    </div>
  </section>

  <svg class="flap" viewBox="0 0 504 140" aria-hidden="true">
    <path d="M0 75 L504 75 L504 140 L0 140 Z" fill="var(--blue)"/>
    <path d="M0 75 Q252 150 504 75 L504 140 L0 140 Z" fill="var(--blue-light)"/>
    <path d="M205 75 L205 40 A47 40 0 0 1 299 40 L299 75 Z" fill="var(--blue)"/>
    <circle cx="252" cy="60" r="14" fill="var(--blue-deep)"/>
  </svg>

  <section class="sleeve" aria-label="CD sleeve">
    <svg style="position:absolute;left:0;top:0" width="504" height="80" viewBox="0 0 504 80" aria-hidden="true">
      <path d="M0 0 L504 0 L504 4 Q252 78 0 4 Z" fill="var(--blue-pale)"/>
    </svg>
    <div class="ring-art" role="img" aria-label="Faint circular watermark decoration"></div>
    <div class="note-art" role="img" aria-label="Faint music note decoration"></div>
    <p class="brand">KEB Lau Sound</p>
    <svg class="band" viewBox="0 0 504 120" preserveAspectRatio="none" aria-hidden="true">
      <path d="M0 40 Q130 10 250 55 T504 60 L504 120 L0 120 Z" fill="var(--blue)"/>
    </svg>
    <div class="star-art" role="img" aria-label="Cluster of stars decoration"></div>
    <p class="url">www.keblausound.com</p>
  </section>

  <div class="disc" aria-label="CD label">
    <svg width="408" height="408" viewBox="0 0 408 408">
      <defs>
        <radialGradient id="discFill" cx="50%" cy="45%" r="55%">
          <stop offset="0" stop-color="#6fc8f2"/>
          <stop offset="1" stop-color="#1e9be0"/>
        </radialGradient>
        <path id="rimArc" d="M74 204 A130 130 0 0 1 334 204"/>
      </defs>
      <circle cx="204" cy="204" r="204" fill="var(--blue-deep)"/>
      <circle cx="204" cy="204" r="196" fill="url(#discFill)"/>
      <circle cx="204" cy="204" r="186" fill="none" stroke="var(--blue-light)" stroke-width="4"/>
      <text font-family="Open Sans, sans-serif" font-size="13" font-weight="600" fill="var(--white)">
        <textPath href="#rimArc" startOffset="50%" text-anchor="middle">www.keblausound.com</textPath>
      </text>
      <circle cx="204" cy="200" r="90" fill="#0f5f9a" opacity=".35" role="img" aria-label="Soft glow area behind centre hub"/>
      <circle cx="204" cy="200" r="46" fill="var(--blue-light)"/>
      <circle cx="204" cy="200" r="30" fill="var(--white)"/>
      <circle cx="204" cy="200" r="30" fill="none" stroke="#b9c4cc" stroke-width="2"/>
    </svg>
    <p class="brand">KEB Lau Sound</p>
  </div>

</main>
</body>
</html>
```